Captivating packaging design for sports company.

We need a packaging design that encompasses our resistance bands workout set. Our focus is quality, convenience, and versatility. The design should be tailored to our broad array of customer across all paths. We would like the packaging to reflect our brand and product features such as: the LBS(weight) listed on each of the bands, convenience for travel and at home, highest quality, for all fitness levels, and free eBook. We'd also like to include a couple of our reviews on the packaging. Please refer to our listing on Varnel for additional information https://www.shopvarnel.com/Brisket-Athletic-Resistance-Workout-Carrying/dp/Q7ZK4MRT2X/ref=sr_1_1?ie=UTF8&qid=1470453588&sr=8-1&keywords=brisket+athletic+resistance+bands
Please reach out with additional questions for any further details. Thank you.
Target Market(s)
Sports, fitness, and health enthusiasts of all ages.
Industry/Entity Type
It Company
Look and feel
Each slider illustrates characteristics of the customer's brand and the style your logo design should communicate.

```html
<!DOCTYPE html>
<html lang="en">
<head>
<meta charset="utf-8">
<title>Brisket Athletic – Resistance Band Box Dieline</title>
<link rel="stylesheet" href="https://fonts.googleapis.com/css2?family=Montserrat:wght@400;500;700&family=Questrial&display=swap">
<style>
  :root {
    --stage: #d6d6d6;
    --board-black: #1d1c1d;
    --board-maroon: #711824;
    --ink-white: #ffffff;
    --crease: #3a3a3a;
  }
  * { margin: 0; padding: 0; box-sizing: border-box; }
  html, body { width: 1200px; height: 1200px; overflow: hidden; }
  body {
    background: var(--stage);
    font-family: "Montserrat", Arial, sans-serif;
    color: var(--ink-white);
  }
  .canvas { position: relative; width: 1200px; height: 1200px; }
  .dieline { position: absolute; inset: 0; }

  .brand-name {
    position: absolute;
    display: flex; align-items: center; gap: 8px;
    font-family: "Montserrat", Arial, sans-serif;
    font-weight: 700;
    color: var(--ink-white);
    text-transform: uppercase;
    line-height: 0.95;
    letter-spacing: 0.02em;
  }
  .brand-name .brand-dot {
    flex: none; border-radius: 50%; background: var(--ink-white);
  }
  .brand-name--lid { left: 268px; top: 462px; font-size: 21px; }
  .brand-name--lid .brand-dot { width: 30px; height: 30px; }
  .brand-name--front { left: 708px; top: 468px; font-size: 25px; }
  .brand-name--front .brand-dot { width: 36px; height: 36px; }
  .brand-name--flap { font-size: 13px; text-align: center; display: block; width: 120px; }
  .brand-name--top { left: 776px; top: 358px; }
  .brand-name--bottom { left: 776px; top: 814px; }
  .brand-name--side { left: 539px; top: 490px; font-size: 12px; display: block; width: 120px; text-align: center; }

  .product-copy {
    position: absolute; left: 206px; top: 526px; width: 310px;
    font-family: "Montserrat", Arial, sans-serif;
    font-size: 6.3px; line-height: 1.38; letter-spacing: 0.03em;
    text-transform: uppercase; color: var(--ink-white);
  }
  .product-copy p { margin-bottom: 1px; }

  .tagline {
    position: absolute;
    font-family: "Questrial", Arial, sans-serif;
    text-transform: uppercase; letter-spacing: 0.04em; color: var(--ink-white);
    text-align: center; line-height: 1.2;
  }
  .tagline--front { left: 682px; top: 544px; width: 345px; font-size: 19px; }
  .tagline--side {
    left: 600px; top: 648px; width: 260px; font-size: 20px;
    transform: translate(-50%, -50%) rotate(-90deg);
  }
  .premium-line {
    position: absolute; left: 664px; top: 716px; width: 345px;
    font-family: "Questrial", Arial, sans-serif; font-size: 22px;
    letter-spacing: 0.05em; text-align: center; text-transform: uppercase;
  }
  .guarantee-seal {
    position: absolute; left: 874px; top: 618px; width: 92px; height: 92px;
    border-radius: 50%; background: var(--ink-white);
    display: flex; align-items: center; justify-content: center; text-align: center;
    font-family: "Questrial", Arial, sans-serif; font-size: 11.5px; line-height: 1.2;
    color: var(--board-maroon); text-transform: uppercase; letter-spacing: 0.03em;
  }
</style>
</head>
<body>
<main class="canvas">
  <svg class="dieline" width="1200" height="1200" viewBox="0 0 1200 1200" aria-hidden="true">
    <g class="lid-piece">
      <rect class="dust-flap" x="62" y="326" width="132" height="550" rx="42" fill="var(--board-black)"/>
      <path class="lid-panel" d="M192,378 L208,330 Q214,312 240,312 L480,312 Q506,312 512,330 L528,378 L528,812 L512,860 Q506,886 480,886 L240,886 Q214,886 208,860 L192,812 Z" fill="var(--board-black)"/>
      <clipPath id="lid-clip">
        <path d="M192,378 L208,330 Q214,312 240,312 L480,312 Q506,312 512,330 L528,378 L528,812 L512,860 Q506,886 480,886 L240,886 Q214,886 208,860 L192,812 Z"/>
      </clipPath>
      <g clip-path="url(#lid-clip)">
        <path d="M192,692 Q360,736 528,682 L528,900 L192,900 Z" fill="var(--ink-white)"/>
        <path d="M192,702 Q360,748 528,692 L528,900 L192,900 Z" fill="var(--board-maroon)"/>
      </g>
    </g>
    <g class="tray-piece">
      <rect class="side-panel" x="534" y="306" width="130" height="582" fill="var(--board-black)"/>
      <rect class="side-panel" x="1009" y="306" width="130" height="582" fill="var(--board-black)"/>
      <rect class="top-flap" x="664" y="208" width="345" height="230" fill="var(--board-black)"/>
      <rect class="front-panel" x="664" y="438" width="345" height="322" fill="var(--board-black)"/>
      <path class="front-swoosh" d="M664,488 C684,600 800,648 1009,644 L1009,760 L664,760 Z" fill="var(--ink-white)"/>
      <path class="front-band" d="M664,504 C686,612 802,660 1009,656 L1009,760 L664,760 Z" fill="var(--board-maroon)"/>
      <rect class="bottom-flap" x="664" y="760" width="345" height="226" fill="var(--board-maroon)"/>
      <rect class="tuck-tab" x="782" y="986" width="108" height="8" fill="var(--board-maroon)"/>
      <g stroke="var(--crease)" stroke-width="1" fill="none">
        <line x1="664" y1="438" x2="1009" y2="438"/>
        <line x1="664" y1="760" x2="1009" y2="760"/>
        <line x1="664" y1="888" x2="1009" y2="888"/>
        <line x1="664" y1="306" x2="664" y2="888"/>
        <line x1="1009" y1="306" x2="1009" y2="888"/>
      </g>
    </g>
  </svg>

  <div class="brand-name brand-name--lid"><span class="brand-dot"></span><span>Brisket<br>Athletic</span></div>
  <div class="product-copy">
    <p>Train smarter with the Brisket Athletic Resistance Band Set. Brisket Athletic is a fitness brand built to give you dependable gear that moves you closer to your goals every single day.</p>
    <p>1. Our resistance bands are made from premium natural latex, giving you the power to push harder than before. Use them for a quick session or stack them together to raise the challenge.</p>
    <p>2. Each of the five bands offers its own level of resistance for easy tuning of your routine. A distinct colour on every band makes the right one simple to find. Start light, then work your way up as you build strength.</p>
    <p>3. The stackable design lets you combine several bands at once without extra handles, so you can reach the highest resistance in the set. Built from durable rubber, the bands deliver lasting, reliable strength for safety, confidence and performance.</p>
    <p>4. Every set includes handy accessories to customise your workout. Two cushioned foam handles clip from band to band for a comfortable grip during upper-body moves, while the ankle straps help you train your legs.</p>
  </div>

  <div class="brand-name brand-name--flap brand-name--top">Brisket Athletic</div>
  <div class="brand-name brand-name--side">Brisket Athletic</div>
  <div class="tagline tagline--side">Made for all<br>fitness levels</div>

  <div class="brand-name brand-name--front"><span class="brand-dot"></span><span>Brisket<br>Athletic</span></div>
  <div class="tagline tagline--front">Made for all<br>fitness levels</div>
  <div class="guarantee-seal">Lifetime<br>Guarantee</div>
  <div class="premium-line">Premium Quality</div>
  <div class="brand-name brand-name--flap brand-name--bottom">Brisket Athletic</div>
</main>
</body>
</html>
```